Re-Design my old Business Card

We need a new business card design. The current layout is lacking good design.
We manufacture building products and also offers services (www.torvalecraft.com.au)
I've attached the old business card to show you what we don't want.
I've also attached the new logo in two styles for you to chose from.
The final design should communicate smarter building design and lifestyle, with a clean and crisp designed card.

Target Market(s)

Architects, building companies

Industry/Entity Type

Business

Contact Information for Business Card

See attached old business cards for all details to include

Font styles to use
Sans Serif

Colors
9bcb3b

Requirements
Must have
• Clean crisp look
Nice to have
• Totally up to you

```html
<!DOCTYPE html>
<html lang="en">
<head>
<meta charset="utf-8">
<title>Torvale Craft – Business Card</title>
<link href="https://fonts.googleapis.com/css2?family=Lato:wght@400;700;900&display=swap" rel="stylesheet">
<style>
  :root {
    --brand-green: #9bcb3b;
    --deep-green: #5e8f22;
    --mid-green: #79a92d;
    --ink: #3a3a3a;
    --muted: #666666;
    --paper: #ffffff;
    --paper-shade: #dddddd;
    --stage: #1f1f1f;
  }
  * { margin: 0; padding: 0; box-sizing: border-box; }
  html, body {
    width: 1200px; height: 873px; overflow: hidden;
    background: var(--stage);
    font-family: "Lato", Arial, sans-serif;
  }
  .stage { position: relative; width: 1200px; height: 873px; }

  .card {
    position: absolute;
    width: 540px; height: 309px;
    border-radius: 4px;
    overflow: hidden;
    box-shadow: 0 18px 40px rgba(0,0,0,.55);
  }

  /* ---------- Front (contact side) ---------- */
  .card-front { left: 70px; top: 110px; background: var(--paper); }
  .card-front .brand {
    position: absolute; left: 44px; top: 112px;
    display: flex; align-items: center; gap: 9px;
    white-space: nowrap;
    color: var(--brand-green);
    font-weight: 900; font-size: 22px; letter-spacing: 1px; text-transform: uppercase;
  }
  .brand-square { width: 16px; height: 16px; background: var(--brand-green); flex: none; }
  .person {
    position: absolute; right: 34px; top: 40px; text-align: right;
    white-space: nowrap;
  }
  .person-name { color: var(--brand-green); font-weight: 900; font-size: 17px; }
  .person-role { color: var(--ink); font-size: 11px; margin-top: 4px; }
  .office-label {
    color: var(--ink); font-size: 11px; margin-top: 8px;
    text-decoration: underline;
  }
  .office-address { color: var(--brand-green); font-weight: 700; font-size: 12px; line-height: 1.5; margin-top: 3px; }

  .contact-tab {
    position: absolute; left: 0; bottom: 26px;
    width: 34px; height: 112px;
    background: var(--brand-green);
    border-radius: 0 6px 6px 0;
    display: flex; flex-direction: column; align-items: center; justify-content: space-around;
    padding: 8px 0;
  }
  .contact-tab svg { width: 14px; height: 14px; fill: var(--paper); }
  .contact-list {
    position: absolute; left: 50px; bottom: 34px;
    list-style: none; color: var(--ink); font-size: 13px; line-height: 24px;
  }
  .corner-band {
    position: absolute; right: 0; bottom: 0; width: 540px; height: 110px;
  }

  /* ---------- Back (brand side) ---------- */
  .card-back { left: 590px; top: 450px; }
  .card-back .pattern {
    position: absolute; inset: 0;
    background: linear-gradient(135deg, var(--mid-green) 0%, var(--deep-green) 55%, #6f9f28 100%);
  }
  .card-back .brand {
    position: absolute; left: 0; right: 0; top: 110px;
    display: flex; align-items: center; justify-content: center; gap: 14px;
    white-space: nowrap;
    color: var(--paper);
    font-weight: 900; font-size: 38px; letter-spacing: 2px; text-transform: uppercase;
  }
  .card-back .brand-square { width: 26px; height: 26px; background: var(--paper); }
  .card-back .rule {
    position: absolute; left: 70px; right: 70px; top: 178px;
    height: 2px; background: var(--paper);
  }
  .website {
    position: absolute; left: 0; right: 0; bottom: 46px; text-align: center;
    color: var(--paper); font-weight: 700; font-size: 16px; letter-spacing: 1px;
  }
</style>
</head>
<body>
<main class="stage">

  <section class="card card-front" aria-label="Business card, contact side">
    <svg class="corner-band" viewBox="0 0 540 110" preserveAspectRatio="none" aria-hidden="true">
      <path d="M0 92 L300 92 Q320 92 330 80 L372 40 Q382 30 400 30 L540 30 L540 110 L0 110 Z" fill="#9bcb3b"/>
      <path d="M0 96 L540 96 L540 110 L0 110 Z" fill="#dddddd"/>
    </svg>

    <div class="brand"><span class="brand-square"></span>Torvale Craft</div>

    <div class="person">
      <p class="person-name">Mark Holloway</p>
      <p class="person-role">Account Manager Qld / Northern NSW</p>
      <p class="office-label">Head Office:</p>
      <p class="office-address">Unit 2/18 Ferris Road<br>Westbrook, QLD 4170</p>
    </div>

    <div class="contact-tab" aria-hidden="true">
      <svg viewBox="0 0 24 24"><path d="M6.6 10.8a15 15 0 0 0 6.6 6.6l2.2-2.2c.3-.3.7-.4 1-.2 1.1.4 2.3.6 3.6.6.6 0 1 .4 1 1V20c0 .6-.4 1-1 1A17 17 0 0 1 3 4c0-.6.4-1 1-1h3.5c.6 0 1 .4 1 1 0 1.3.2 2.5.6 3.6.1.3 0 .7-.2 1z"/></svg>
      <svg viewBox="0 0 24 24"><path d="M7 2h10a2 2 0 0 1 2 2v16a2 2 0 0 1-2 2H7a2 2 0 0 1-2-2V4a2 2 0 0 1 2-2zm0 3v13h10V5z"/></svg>
      <svg viewBox="0 0 24 24"><path d="M6 3h12v5H6zM4 9h16a2 2 0 0 1 2 2v6h-4v4H6v-4H2v-6a2 2 0 0 1 2-2zm4 6v4h8v-4z"/></svg>
      <svg viewBox="0 0 24 24"><path d="M2 5h20v14H2zm2 2v.5l8 5 8-5V7z"/></svg>
    </div>
    <ul class="contact-list">
      <li>1300 555 210</li>
      <li>0400 555 816</li>
      <li>1300 555 211</li>
      <li>mark@torvalecraft.com.au</li>
    </ul>
  </section>

  <section class="card card-back" aria-label="Business card, brand side">
    <div class="pattern" role="img" aria-label="Faceted green low-poly background pattern"></div>
    <div class="brand"><span class="brand-square"></span>Torvale Craft</div>
    <div class="rule"></div>
    <p class="website">www.torvalecraft.com.au</p>
  </section>

</main>
</body>
</html>
```